Web Page Design for a Website that Provides Tutoring

I am looking to create an online tutoring website. The website will allow parents or students to contact tutors with a view to instructing them to tutor themselves or their children.

The name of the website is LendYourLessons.

This brief is to create the design for one of the web pages for this web site. I am hoping the same designer will be available to design other pages.

The page I want designed is one of the more complex and I have attached the design as an excel spreadsheet. The web page needs to include all the items on this page but if you want to change the positioning of the items then Im fine with that.

I recently had two logos created for this website. My favourite is the one with a mortar board but im not sure I like the colours. I have attached both of these logos and you can use either of them, change the colours or create something different. I just want a design pleasing to the eye. If the logo is changed I would like that in a seperate file.

So can you please submit designs for this page. I have attached the two logos which you can use, change or if you feel you have a better idea then you can use that.

On the spreadsheet the Send Message, Favourite etc are buttons.

Target Market(s)

People who want to better themselves.
Possible middle class to upper class.

Industry/Entity Type

Tutoring

Number of Pages Required

1 page

Requirements
Must have
• The designs must have alot of the information attached in the spreadsheet.

```html
<!DOCTYPE html>
<html lang="en">
<head>
<meta charset="utf-8">
<title>LendYourLessons – Tutor Profile</title>
<link rel="stylesheet" href="https://fonts.googleapis.com/css2?family=Lato:wght@400;700;900&family=Open+Sans:wght@400;600;700&display=swap">
<style>
  :root{
    --green:#63a868;
    --green-dark:#4f9455;
    --orange:#f7941d;
    --page:#ebebeb;
    --card:#ffffff;
    --ink:#2b2b2b;
    --muted:#666;
    --line:#d9d9d9;
    --red:#e2463d;
    --blue:#4b8fd6;
    --grey-btn:#8a8a8a;
  }
  *{box-sizing:border-box;margin:0;padding:0}
  html,body{width:1200px;height:2390px;overflow:hidden}
  body{position:relative;background:var(--page);font-family:"Open Sans",Arial,sans-serif;color:var(--ink)}
  .abs{position:absolute}

  /* hero */
  .hero{left:0;top:0;width:1200px;height:440px;background:linear-gradient(100deg,#a35a3a 0%,#c9825f 25%,#5a4038 50%,#c0634f 70%,#d9d4cf 100%)}
  .hero-title{left:0;top:290px;width:1200px;text-align:center;font-family:"Lato",sans-serif;font-weight:900;font-size:48px;letter-spacing:1px;color:#fff}
  .hero-rule{left:330px;top:342px;width:540px;height:2px;background:#fff}

  /* header */
  .header-band{left:0;top:440px;width:1200px;height:121px;background:var(--green)}
  .brand{left:172px;top:440px;width:270px;height:121px;background:#fff;display:flex;align-items:center;justify-content:center;gap:8px}
  .brand-mark{width:14px;height:14px;background:var(--orange)}
  .brand-name{font-family:"Lato",sans-serif;font-weight:700;font-size:27px;color:var(--orange)}
  .contact-row{left:478px;top:460px;display:flex;gap:30px;font-size:11px;color:#fff;align-items:center}
  .contact-row span{display:flex;align-items:center;gap:8px}
  .header-rule{left:462px;top:493px;width:563px;height:1px;background:rgba(255,255,255,.35)}
  .login{left:939px;top:456px;width:78px;height:22px;border-radius:11px;background:#fff;color:var(--ink);font-family:"Lato",sans-serif;font-weight:700;font-size:11px;display:flex;align-items:center;justify-content:center}
  .main-nav{left:476px;top:518px;display:flex;gap:0;font-family:"Lato",sans-serif;font-weight:700;font-size:11.5px;color:#fff}
  .main-nav a{color:#fff;text-decoration:none;display:block;margin-right:44px;padding-bottom:8px}
  .main-nav a.current{border-bottom:2px solid #fff}
  .pager{left:918px;top:561px;height:34px;display:flex;font-size:13px;color:#fff}
  .pager span{background:var(--grey-btn);padding:0 12px;display:flex;align-items:center}
  .pager span+span{border-left:1px solid #9e9e9e}

  /* cards */
  .card{position:absolute;background:var(--card);box-shadow:0 1px 2px rgba(0,0,0,.08)}
  .card-title{position:absolute;left:27px;top:30px;font-family:"Lato",sans-serif;font-weight:700;font-size:17px;color:var(--ink);letter-spacing:.3px}
  .card-tools{position:absolute;right:27px;top:36px;display:flex;gap:1px}
  .card-tools i{width:9px;height:8px;border:1px solid #999;display:block}

  /* profile */
  .profile{left:172px;top:630px;width:563px;height:295px}
  .profile-photo{position:absolute;left:0;top:0;width:209px;height:295px;background:linear-gradient(160deg,#d9d6d0 0%,#c9b7a6 45%,#7d7f9a 100%)}
  .tutor-label{position:absolute;left:230px;top:33px;font-family:"Lato",sans-serif;font-weight:700;font-size:12px;color:var(--orange)}
  .tutor-name{position:absolute;left:230px;top:52px;font-family:"Lato",sans-serif;font-weight:700;font-size:17px;letter-spacing:.5px}
  .tutor-bio{position:absolute;left:230px;top:106px;width:310px;font-size:12.4px;line-height:19px;color:#555;text-align:justify}

  /* actions */
  .actions{left:172px;top:948px;width:563px;height:147px}
  .btn-row{position:absolute;left:27px;top:26px;display:flex;gap:9px}
  .pill{height:28px;padding:0 16px;border-radius:14px;border:1px solid #bbb;font-family:"Lato",sans-serif;font-weight:700;font-size:10.5px;display:flex;align-items:center;color:var(--ink);background:#fff}
  .pill.active{background:var(--green);border-color:var(--green);color:#fff}
  .msg-input{position:absolute;left:27px;top:80px;width:434px;height:32px;border:1px solid #ccc;font-size:12px;color:#666;padding:0 12px;display:flex;align-items:center}
  .send-btn{position:absolute;left:467px;top:80px;width:69px;height:32px;background:var(--orange);color:#fff;font-family:"Lato",sans-serif;font-weight:700;font-size:12px;display:flex;align-items:center;justify-content:center}

  /* tables */
  table{border-collapse:collapse;position:absolute}
  td,th{border:1px solid var(--line)}
  .subjects{left:172px;top:1117px;width:563px;height:233px}
  .price-table{left:27px;top:75px;width:509px;font-size:11px}
  .price-table th{height:43px;font-weight:400;color:#555;text-align:right;vertical-align:bottom;padding:0 6px 4px;font-size:11px;line-height:12px}
  .price-table td{height:40px;text-align:right;padding:0 8px;color:#888}
  .price-table td.subject{text-align:left;font-family:"Lato",sans-serif;font-weight:700;color:var(--ink);font-size:11px;padding-left:8px;width:97px}
  .price-table td.price{color:var(--green)}

  .availability{left:172px;top:1376px;width:563px;height:306px}
  .avail-table{left:27px;top:76px;width:509px;font-size:11px}
  .avail-table th{height:28px;font-weight:400;color:#555;text-align:right;padding:0 6px;font-size:11px}
  .avail-table td{height:27px;text-align:center}
  .avail-table td.slot{text-align:left;padding-left:10px;font-family:"Lato",sans-serif;font-weight:700;font-size:10.5px;width:67px}
  .avail-table svg{display:block;margin:0 auto}
  .legend{position:absolute;left:27px;top:262px;display:flex;gap:36px;font-size:11px;color:#555}
  .legend span{display:flex;align-items:center;gap:14px}

  /* right column */
  .rating{left:759px;top:630px;width:266px;height:248px}
  .details{left:759px;top:902px;width:266px;height:466px}
  .start-rating{left:759px;top:1395px;width:266px;height:298px}
  .stat-list{position:absolute;left:25px;width:213px}
  .stat{height:37px;border:1px solid #dcdcdc;display:flex;align-items:center;justify-content:space-between;padding:0 10px;font-size:10.5px;margin-bottom:12px}
  .stat b{font-family:"Lato",sans-serif;font-weight:700;font-size:10.5px;color:var(--ink)}
  .stat .o{color:var(--orange);font-size:12px}
  .stat .g{color:var(--green);font-size:12px}
  .feedback-btn{position:absolute;left:25px;top:386px;width:213px;height:43px;background:var(--orange);color:#fff;font-family:"Lato",sans-serif;font-weight:700;font-size:13px;letter-spacing:.5px;display:flex;align-items:center;justify-content:center}

  .field{position:absolute;left:25px;top:76px;width:213px;height:35px;border:1px solid #ccc;font-size:10.5px;color:#777;padding:0 10px;display:flex;align-items:center;letter-spacing:.3px}
  .label{position:absolute;font-size:10.5px;color:#666;letter-spacing:.3px}
  .box-row{position:absolute;display:flex;gap:3px;align-items:center;font-size:10px;color:#888}
  .box-row i{width:14px;height:21px;border:1px solid #ccc;display:block}
  .stars{position:absolute;left:113px;top:189px;display:flex;gap:2px}
  .submit-btn{position:absolute;left:25px;top:220px;width:213px;height:43px;background:var(--green);color:#fff;font-family:"Lato",sans-serif;font-weight:700;font-size:13px;letter-spacing:.5px;display:flex;align-items:center;justify-content:center}

  /* reviews */
  .reviews{left:172px;top:1723px;width:853px;height:357px}
  .reviews-sub{position:absolute;left:27px;top:74px;font-size:12px;color:#555}
  .reviews-sub em{font-style:normal;color:var(--orange)}
  .review{position:absolute;left:42px;width:780px;display:flex;gap:16px}
  .avatar{flex:none;width:34px;height:34px;border-radius:50%;background:#a79a86;color:#fff;font-family:"Lato",sans-serif;font-size:18px;display:flex;align-items:center;justify-content:center}
  .review-body{padding-top:2px}
  .review-stars{display:flex;gap:1px;margin-bottom:6px}
  .review-text{font-size:11px;line-height:15px;color:#555;width:730px}
  .review-by{font-size:10.5px;color:#777;margin-top:14px}

  /* footer */
  .footer{left:0;top:2144px;width:1200px;height:246px;background:linear-gradient(120deg,#8a4a2a 0%,#b06b43 45%,#c48059 70%,#9a5734 100%)}
  .footer-brand{left:0;top:2230px;width:1200px;text-align:center;font-family:"Lato",sans-serif;font-weight:700;font-size:27px;color:#fff}
  .footer-rule{left:460px;top:2300px;width:280px;height:1px;background:rgba(255,255,255,.25)}
  .copyright{left:180px;top:2347px;font-size:10px;color:#fff}
  .social{left:578px;top:2348px;display:flex;gap:7px}
  .social i{width:8px;height:8px;border-radius:50%;background:#fff;display:block}
  .footer-nav{left:682px;top:2346px;display:flex;gap:25px;font-family:"Lato",sans-serif;font-weight:700;font-size:11px;color:#fff}
  .to-top{left:1057px;top:2333px;width:30px;height:30px;border:1.5px solid #fff;border-radius:50%;display:flex;align-items:center;justify-content:center}
</style>
</head>
<body>
<svg width="0" height="0" style="position:absolute">
  <defs>
    <symbol id="ico-tick" viewBox="0 0 12 12"><circle cx="6" cy="6" r="5.5" fill="#63a868"/><path d="M3.3 6.2 5.2 8 8.8 4.3" fill="none" stroke="#fff" stroke-width="1.6"/></symbol>
    <symbol id="ico-taken" viewBox="0 0 12 12"><circle cx="6" cy="6" r="5.5" fill="#e2463d"/><path d="M4 4 8 8M8 4 4 8" stroke="#fff" stroke-width="1.5"/></symbol>
    <symbol id="ico-reserved" viewBox="0 0 12 12"><circle cx="6" cy="6" r="5.5" fill="#f7941d"/><path d="M3.5 6h5" stroke="#fff" stroke-width="1.6"/></symbol>
    <symbol id="ico-no" viewBox="0 0 20 4"><rect x="0" y="1" width="20" height="2" fill="#4b8fd6"/></symbol>
    <symbol id="ico-star" viewBox="0 0 20 20"><polygon points="10,1 12.6,7.2 19.3,7.6 14.2,11.9 15.8,18.5 10,14.9 4.2,18.5 5.8,11.9 0.7,7.6 7.4,7.2"/></symbol>
  </defs>
</svg>

<div class="abs hero" role="img" aria-label="Photo of two students sitting back to back with laptops in a library"></div>
<div class="abs hero-title">EXPLORE, SHARE &amp; LEARN</div>
<div class="abs hero-rule"></div>

<header>
  <div class="abs header-band"></div>
  <div class="abs brand"><span class="brand-mark"></span><span class="brand-name">LendYourLessons</span></div>
  <div class="abs contact-row">
    <span><svg width="10" height="10" viewBox="0 0 10 10"><path d="M2 0.5 3.8 2.6 2.9 3.9Q4 6 6.1 7.1L7.4 6.2 9.5 8 8.3 9.5Q3.5 9 0.5 1.7Z" fill="#fff"/></svg>+00 000 000 0000</span>
    <span><svg width="11" height="8" viewBox="0 0 11 8"><rect width="11" height="8" fill="#fff"/><path d="M0 0 5.5 4.5 11 0" fill="none" stroke="#63a868" stroke-width="1"/></svg>info@lendyourlessons.com</span>
  </div>
  <div class="abs login">LOG IN</div>
  <div class="abs header-rule"></div>
  <nav class="abs main-nav">
    <a>HOME</a><a class="current">SEARCH</a><a>STUDENT</a><a>TUTOR</a><a>ABOUT</a><a>CONTACT</a>
  </nav>
</header>

<div class="abs pager"><span>Prev</span><span>Next</span></div>

<section class="card profile">
  <div class="profile-photo" role="img" aria-label="Portrait photo of the tutor at a laptop"></div>
  <div class="tutor-label">TUTOR'S NAME</div>
  <div class="tutor-name">OWEN MARLOW</div>
  <p class="tutor-bio">Lorem ipsum dolor sit amet, consectetur adipiscing elit, sed do eiusmod tempor incid idunt ut labore et dolore magna aliqua. Ut enim ad minim veniam, quis nost rud exerc itation ullamco laboris nisi ut aliquip ex ea comm odo consequat. Duis aute irure dolor in reprehenderit in volu ptate Excepteur sint occaecat cupidatat non proident, sunt in culpa qui officia deserunt.</p>
</section>

<section class="card actions">
  <div class="btn-row">
    <span class="pill active">SEND MESSAGE</span>
    <span class="pill">FAVOUR TUTOR</span>
    <span class="pill">WRITE REVIEW</span>
  </div>
  <div class="card-tools" style="top:36px"><i></i><i></i></div>
  <div class="msg-input">Write here...</div>
  <div class="send-btn">SEND</div>
</section>

<section class="card subjects">
  <h2 class="card-title">SUBJECTS TAUGHT</h2>
  <div class="card-tools"><i></i><i></i></div>
  <table class="price-table">
    <tr><th></th><th>Primary</th><th>Secondary</th><th>GCSE</th><th>A-Level</th><th>University</th><th>Adult<br>Learner</th></tr>
    <tr><td class="subject">BIOLOGY</td><td class="price">£20</td><td>–</td><td class="price">£25</td><td class="price">£30</td><td>–</td><td>–</td></tr>
    <tr><td class="subject">CHEMISTRY</td><td class="price">£20</td><td>–</td><td class="price">£25</td><td class="price">£30</td><td>–</td><td>–</td></tr>
  </table>
</section>

<section class="card availability">
  <h2 class="card-title">AVAILABILITY</h2>
  <div class="card-tools"><i></i><i></i></div>
  <table class="avail-table">
    <tr><th></th><th>Mon</th><th>Tue</th><th>Wed</th><th>Thu</th><th>Fri</th><th>Sat</th><th>Sun</th></tr>
    <tr><td class="slot">7-8 AM</td>
      <td><svg width="11" height="11"><use href="#ico-tick"/></svg></td><td><svg width="11" height="11"><use href="#ico-tick"/></svg></td><td><svg width="11" height="11"><use href="#ico-tick"/></svg></td><td><svg width="11" height="11"><use href="#ico-tick"/></svg></td><td><svg width="11" height="11"><use href="#ico-tick"/></svg></td><td><svg width="11" height="11"><use href="#ico-tick"/></svg></td><td><svg width="11" height="11"><use href="#ico-tick"/></svg></td></tr>
    <tr><td class="slot">8-9 AM</td>
      <td><svg width="11" height="11"><use href="#ico-tick"/></svg></td><td><svg width="11" height="11"><use href="#ico-tick"/></svg></td><td><svg width="11" height="11"><use href="#ico-tick"/></svg></td><td><svg width="11" height="11"><use href="#ico-taken"/></svg></td><td><svg width="11" height="11"><use href="#ico-tick"/></svg></td><td><svg width="11" height="11"><use href="#ico-taken"/></svg></td><td><svg width="11" height="11"><use href="#ico-tick"/></svg></td></tr>
    <tr><td class="slot">4-5 PM</td>
      <td><svg width="11" height="11"><use href="#ico-tick"/></svg></td><td><svg width="11" height="11"><use href="#ico-taken"/></svg></td><td><svg width="11" height="11"><use href="#ico-tick"/></svg></td><td><svg width="11" height="11"><use href="#ico-tick"/></svg></td><td><svg width="11" height="11"><use href="#ico-tick"/></svg></td><td><svg width="11" height="11"><use href="#ico-tick"/></svg></td><td><svg width="18" height="4"><use href="#ico-no"/></svg></td></tr>
    <tr><td class="slot">5-6 PM</td>
      <td><svg width="11" height="11"><use href="#ico-tick"/></svg></td><td><svg width="11" height="11"><use href="#ico-tick"/></svg></td><td><svg width="11" height="11"><use href="#ico-tick"/></svg></td><td><svg width="11" height="11"><use href="#ico-tick"/></svg></td><td><svg width="11" height="11"><use href="#ico-taken"/></svg></td><td><svg width="11" height="11"><use href="#ico-reserved"/></svg></td><td><svg width="11" height="11"><use href="#ico-tick"/></svg></td></tr>
    <tr><td class="slot">7-8 PM</td>
      <td><svg width="11" height="11"><use href="#ico-tick"/></svg></td><td><svg width="11" height="11"><use href="#ico-tick"/></svg></td><td><svg width="11" height="11"><use href="#ico-tick"/></svg></td><td><svg width="11" height="11"><use href="#ico-tick"/></svg></td><td><svg width="11" height="11"><use href="#ico-tick"/></svg></td><td><svg width="11" height="11"><use href="#ico-tick"/></svg></td><td><svg width="11" height="11"><use href="#ico-tick"/></svg></td></tr>
  </table>
  <div class="legend">
    <span><svg width="11" height="11"><use href="#ico-tick"/></svg>Available</span>
    <span><svg width="11" height="11"><use href="#ico-taken"/></svg>Taken</span>
    <span><svg width="11" height="11"><use href="#ico-reserved"/></svg>Reserved</span>
    <span><svg width="18" height="4"><use href="#ico-no"/></svg>No</span>
  </div>
</section>

<aside>
  <section class="card rating">
    <h2 class="card-title">RATING</h2>
    <div class="card-tools"><i></i><i></i></div>
    <div class="stat-list" style="top:79px">
      <div class="stat"><b>REVIEW SCORE</b><span class="o">4.5/5</span></div>
      <div class="stat"><b>RELIABILITY</b><span class="o">4.0 / 5.0</span></div>
      <div class="stat"><b>PUNCTUALITY</b><span class="o">4.6/5</span></div>
    </div>
  </section>

  <section class="card details">
    <h2 class="card-title">DETAILS</h2>
    <div class="card-tools"><i></i><i></i></div>
    <div class="stat-list" style="top:77px">
      <div class="stat"><b>TUTORING TYPE</b><span class="g">In personal only</span></div>
      <div class="stat"><b>WILLING TO TRAVEL</b><span class="g">Home Only</span></div>
      <div class="stat"><b>AGE</b><span class="g">24</span></div>
      <div class="stat"><b>DBS (CRB)</b><span class="g">Verified</span></div>
      <div class="stat"><b>MEMBER SINCE</b><span class="g">11 months ago</span></div>
      <div class="stat"><b>LAST LOGGED IN</b><span class="g">2 days ago</span></div>
    </div>
    <div class="feedback-btn">LEAVE FEEDBACK</div>
  </section>

  <section class="card start-rating">
    <h2 class="card-title">START RATING</h2>
    <div class="card-tools"><i></i><i></i></div>
    <div class="field">ENTER TUTEE NAME</div>
    <div class="label" style="left:25px;top:127px">ENTER DATE</div>
    <div class="label" style="left:165px;top:127px">ENTER TIME</div>
    <div class="box-row" style="left:25px;top:144px"><i></i><i></i>/<i></i><i></i>/<i></i><i></i></div>
    <div class="box-row" style="left:165px;top:144px"><i></i><i></i>:<i></i><i></i></div>
    <div class="label" style="left:25px;top:191px">START RATING</div>
    <div class="stars">
      <svg width="18" height="18" fill="#d0d0d0"><use href="#ico-star"/></svg>
      <svg width="18" height="18" fill="#d0d0d0"><use href="#ico-star"/></svg>
      <svg width="18" height="18" fill="#d0d0d0"><use href="#ico-star"/></svg>
      <svg width="18" height="18" fill="#d0d0d0"><use href="#ico-star"/></svg>
      <svg width="18" height="18" fill="#d0d0d0"><use href="#ico-star"/></svg>
    </div>
    <div class="submit-btn">SUBMIT</div>
  </section>
</aside>

<section class="card reviews">
  <h2 class="card-title" style="top:37px">OWEN'S REVIEWS</h2>
  <div class="card-tools" style="top:42px"><i></i><i></i></div>
  <p class="reviews-sub">Tutors Name has <em>2</em> reviews with an average review of <em>4.0</em></p>
  <article class="review" style="top:118px">
    <div class="avatar">P</div>
    <div class="review-body">
      <div class="review-stars">
        <svg width="8" height="8" fill="#f7b51d"><use href="#ico-star"/></svg><svg width="8" height="8" fill="#f7b51d"><use href="#ico-star"/></svg><svg width="8" height="8" fill="#f7b51d"><use href="#ico-star"/></svg><svg width="8" height="8" fill="#f7b51d"><use href="#ico-star"/></svg><svg width="8" height="8" fill="#f7b51d"><use href="#ico-star"/></svg>
      </div>
      <p class="review-text">Lorem ipsum dolor sit amet, consectetur adipiscing elit, sed do eiusmod tempor incididunt ut labore et dolore magna aliqua. Ut enim ad minim veniam, quis nostrud exercitation ullamco laboris nisi ut aliquip ex ea commodo consequat. Duis aute irure dolor in repreh enderit in voluptate velit esse cillum.</p>
      <p class="review-by">by Priya on Dec 03, 2016</p>
    </div>
  </article>
  <article class="review" style="top:228px">
    <div class="avatar">D</div>
    <div class="review-body">
      <div class="review-stars">
        <svg width="8" height="8" fill="#f7b51d"><use href="#ico-star"/></svg><svg width="8" height="8" fill="#f7b51d"><use href="#ico-star"/></svg><svg width="8" height="8" fill="#f7b51d"><use href="#ico-star"/></svg><svg width="8" height="8" fill="#f7b51d"><use href="#ico-star"/></svg><svg width="8" height="8" fill="#f7b51d"><use href="#ico-star"/></svg>
      </div>
      <p class="review-text">Lorem ipsum dolor sit amet, consectetur adipiscing elit, sed do eiusmod tempor incididunt ut labore et dolore magna aliqua. Ut enim ad minim veniam, quis nostrud exercitation ullamco laboris nisi ut aliquip ex ea commodo consequat. Duis aute irure dolor in repreh enderit in voluptate velit esse cillum.</p>
      <p class="review-by">by Daniel on May 15, 2016</p>
    </div>
  </article>
</section>

<footer>
  <div class="abs footer" role="img" aria-label="Warm-toned photo of hands writing at a desk"></div>
  <div class="abs footer-brand">LendYourLessons</div>
  <div class="abs footer-rule"></div>
  <div class="abs copyright">Copyright © Lend Your Lessons 2016</div>
  <div class="abs social"><i></i><i></i><i></i></div>
  <nav class="abs footer-nav"><span>HOME</span><span>SEARCH</span><span>STUDENT</span><span>TUTOR</span><span>ABOUT</span><span>CONTACT</span></nav>
  <div class="abs to-top"><svg width="12" height="8" viewBox="0 0 12 8"><path d="M1 7 6 2 11 7" fill="none" stroke="#fff" stroke-width="1.6"/></svg></div>
</footer>
</body>
</html>
```